Sports Nutrition Supplement Label design

We need a sports supplement label design for an existing business. (I have provided our business logo in the file uploads) These labels will remain consistent across the product line with the name of the product being the only changing field. The current product names (example: "vegan") on the labels provided are just for reference, the ingredients portions etc are final, but the actual name will be changed to something less generic for each product. I will just need to be able to change the name and have it match with label concept. We would like the look to be professional, clean, and exemplify quality. Please reference our business website tidelinevigor.com to get a feel for design and brand association.
I have also included the NKB supplement label guidelines so we are certain to maintain compliance.
Thank you and I'm looking forward to working with you and seeing your creative designs!
Darin

Target Market(s)

Athletes, Sports professionals, Colleges, Professional Sports Teams

Industry/Entity Type

Sports Science/ Sports Training/Athletics

Requirements
Nice to have
• I would like the design to possibly reflect these key terms: Sport Science, Chemistry, Clean, Professional, Quality (We also like water/ocean/waves concepts but is not a "requirement" it would have to really work well in the design somehow to appeal to wide range of athletes)

```html
<!DOCTYPE html>
<html lang="en">
<head>
<meta charset="UTF-8">
<title>Tideline Vigor – Vegan Chocolate Milk Shake Label</title>
<link rel="stylesheet" href="https://fonts.googleapis.com/css2?family=Alfa+Slab+One&family=Great+Vibes&family=Montserrat:wght@400;500;800&family=Roboto+Condensed:wght@500&display=swap">
<style>
  :root {
    --page-bg: #f4f4f4;
    --label-red: #a8141c;
    --label-red-light: #c2232a;
    --label-red-dark: #6f0b10;
    --ink-white: #ffffff;
  }
  * { margin: 0; padding: 0; box-sizing: border-box; }
  html, body {
    width: 1200px;
    height: 1200px;
    overflow: hidden;
    background: var(--page-bg);
  }
  .canvas {
    position: relative;
    width: 1200px;
    height: 1200px;
  }
  .label {
    position: absolute;
    left: 100px;
    top: 220px;
    width: 1000px;
    height: 760px;
    overflow: hidden;
    background:
      radial-gradient(ellipse 65% 60% at 40% 58%, var(--label-red-light) 0%, var(--label-red) 55%, var(--label-red-dark) 100%);
    color: var(--ink-white);
    text-align: center;
  }
  .brand {
    position: absolute;
    top: 62px;
    left: 0;
    width: 100%;
    font-family: "Montserrat", sans-serif;
    font-weight: 400;
    line-height: 1;
  }
  .brand-main {
    display: block;
    font-size: 74px;
    letter-spacing: 0.1em;
    padding-left: 0.1em;
  }
  .brand-sub {
    display: block;
    margin-top: 14px;
    font-size: 28px;
    letter-spacing: 0.32em;
    padding-left: 0.32em;
  }
  .product-name {
    position: absolute;
    top: 240px;
    left: 0;
    width: 100%;
    font-family: "Alfa Slab One", serif;
    font-weight: 400;
    font-size: 140px;
    line-height: 1;
    letter-spacing: 0.01em;
  }
  .flavor {
    position: absolute;
    top: 430px;
    left: 0;
    width: 100%;
    height: 170px;
  }
  .flavor-main {
    position: absolute;
    left: 236px;
    top: 0;
    font-family: "Great Vibes", cursive;
    font-size: 110px;
    line-height: 1;
    transform: rotate(-6deg);
    transform-origin: left center;
  }
  .flavor-sub {
    position: absolute;
    left: 372px;
    top: 98px;
    white-space: nowrap;
    line-height: 1;
  }
  .flavor-sub-bold {
    font-family: "Montserrat", sans-serif;
    font-weight: 800;
    font-size: 38px;
    letter-spacing: 0.02em;
  }
  .flavor-sub-script {
    font-family: "Great Vibes", cursive;
    font-size: 64px;
    margin-left: 6px;
  }
  .flavor-note {
    position: absolute;
    top: 632px;
    left: 0;
    width: 100%;
    font-family: "Montserrat", sans-serif;
    font-weight: 500;
    font-size: 40px;
    line-height: 1;
  }
  .net-weight {
    position: absolute;
    top: 700px;
    left: 0;
    width: 100%;
    font-family: "Roboto Condensed", sans-serif;
    font-weight: 500;
    font-size: 22px;
    letter-spacing: 0.02em;
    line-height: 1;
  }
</style>
</head>
<body>
<main class="canvas">
  <section class="label">
    <p class="brand">
      <span class="brand-main">TIDELINE</span>
      <span class="brand-sub">VIGOR</span>
    </p>
    <h1 class="product-name">VEGAN</h1>
    <div class="flavor">
      <span class="flavor-main">Chocolate</span>
      <span class="flavor-sub"><span class="flavor-sub-bold">MILK</span><span class="flavor-sub-script">shake</span></span>
    </div>
    <p class="flavor-note">Natural Flavor</p>
    <p class="net-weight">DIETARY SUPPLEMENT | NET WT.&nbsp; 907 G&nbsp; (2 LB)</p>
  </section>
</main>
</body>
</html>
```